PDBA website design

We need a page template website design for a cms website. Please see the brief attached for the details.
The client is the Pacific Downhorn Breeders Association which is an organisation promoting the White Suffolk Sheep Breed within Australia.

Reason: So that my top few designs can make changes and re-submit.

Target Market(s)

See attached brief

```html
<!DOCTYPE html>
<html lang="en">
<head>
<meta charset="utf-8">
<title>Pacific Downhorn Breeders Association</title>
<link rel="stylesheet" href="https://fonts.googleapis.com/css2?family=Ubuntu:wght@300;400;500;700&display=swap">
<style>
:root{
  --orange:#e07f00;
  --orange-text:#f0a320;
  --dark:#333333;
  --green:#4c9a14;
  --text:#444444;
  --blue:#2d7fd6;
  --white:#ffffff;
  --sky:#7fa9d6;
  --field:#c98e45;
}
*{margin:0;padding:0;box-sizing:border-box}
html,body{width:931px;height:1200px;overflow:hidden}
body{font-family:"Ubuntu",sans-serif;color:var(--text);background:#ffffff}
.stage{position:absolute;left:0;top:0;width:1024px;height:1320px;transform:scale(0.90918,0.90909);transform-origin:0 0}
.backdrop{position:absolute;inset:0;background:linear-gradient(180deg,var(--sky) 0%,var(--field) 100%)}
.page{position:absolute;left:84px;top:0;width:852px;height:1320px;background:var(--white);box-shadow:0 0 14px rgba(0,0,0,.45)}
.header{position:absolute;left:0;top:0;width:852px;height:145px;border-bottom:1px solid #cfcfcf}
.brand{position:absolute;left:48px;top:50px;display:flex;align-items:center;gap:10px}
.brand-mark{width:34px;height:34px;background:var(--green)}
.brand-name{font-size:30px;font-weight:500;color:var(--green)}
.site-title{position:absolute;left:289px;top:54px;font-size:28px;font-weight:400;color:#333;letter-spacing:.3px}
.hero{position:absolute;left:0;top:146px;width:852px;height:359px;background:linear-gradient(180deg,#8d9fa6 0%,#5e8a3f 100%)}
.hero-arrow{position:absolute;top:154px;width:36px;height:50px;background:rgba(90,80,30,.75)}
.hero-arrow.prev{left:0}.hero-arrow.next{right:0}
.nav{position:absolute;left:0;top:505px;width:852px;height:47px;background:linear-gradient(180deg,#3c3c3c,#2b2b2b);display:flex}
.nav a{display:block;height:47px;line-height:47px;text-align:center;color:#fff;font-size:14.5px;text-decoration:none;border-right:1px solid #222;text-shadow:0 1px 1px rgba(0,0,0,.6)}
.nav a.active{background:var(--orange)}
.dropdown{position:absolute;left:169px;top:553px;width:129px}
.dropdown a{display:block;height:46px;line-height:46px;padding-left:19px;color:#fff;font-size:14px;text-decoration:none}
.dropdown .member{background:#424242}
.dropdown .stud{background:var(--orange)}
.tiles{position:absolute;top:574px;left:0;width:852px;height:144px}
.tile{position:absolute;top:0;width:193px;height:144px;border:1px solid #cfcfcf;box-shadow:0 1px 3px rgba(0,0,0,.25);overflow:hidden}
.tile .photo{position:absolute;inset:0 0 44px 0}
.tile .caption{position:absolute;left:0;bottom:0;width:100%;height:44px;background:#3a3a3a;color:var(--orange-text);font-size:13.5px;display:flex;align-items:center;justify-content:center;text-align:center;line-height:16px}
.content{position:absolute;left:18px;top:748px;width:605px}
h2{font-size:21px;font-weight:400;color:#555}
h2 b{color:var(--green);font-weight:500}
.intro{margin-top:8px;font-size:14px;font-weight:300;line-height:20px;color:#333;letter-spacing:.15px}
.aims{margin-top:23px;font-size:14px;font-weight:300;color:#333}
.aims span{color:var(--green);font-weight:400}
.aims-list{list-style:none;margin-top:10px}
.aims-list li{position:relative;padding-left:26px;font-size:14px;font-weight:300;line-height:20px;color:#333;margin-bottom:10px}
.aims-list svg{position:absolute;left:8px;top:5px}
.btn{position:absolute;left:19px;top:1094px;width:132px;height:41px;background:var(--orange);color:#fff;font-size:14px;font-weight:500;text-decoration:none;display:flex;align-items:center;padding-left:14px;gap:10px}
.sidebar{position:absolute;left:639px;top:748px;width:196px}
.sponsor-box{margin-top:11px;width:195px;height:259px;border:1px solid #cfcfcf;position:relative;background:#fff}
.sponsor-bar{position:absolute;left:0;width:100%;height:23px;background:#3a3a3a;display:flex;align-items:center;justify-content:center}
.sponsor-bar.top{top:0}.sponsor-bar.bottom{bottom:0}
.sponsor{position:absolute;left:0;width:100%;height:98px;display:flex;align-items:center;justify-content:center;gap:8px;font-size:19px;font-weight:400;color:#333}
.sponsor.one{top:23px;border-bottom:1px dashed #cccccc}
.sponsor.two{top:121px}
.sponsor .dot{width:18px;height:18px;background:#1e7fbf;border-radius:50%}
.sponsor.one .dot{border-radius:0;background:var(--orange)}
.social{margin-top:26px;width:195px;height:66px;background:var(--blue);border:1px solid #1f6bbf;position:relative;color:#fff}
.social .sq{position:absolute;left:14px;top:23px;width:18px;height:18px;background:#fff}
.social .divider{position:absolute;left:45px;top:10px;width:1px;height:46px;background:rgba(255,255,255,.35)}
.social .count{position:absolute;left:58px;top:13px;font-size:14px;white-space:nowrap}
.social .follow{position:absolute;left:58px;top:36px;font-size:14px;text-decoration:underline;white-space:nowrap}
.footer{position:absolute;left:0;top:1196px;width:852px;height:124px;background:linear-gradient(180deg,#3c8c10,#2f6f0a);border-top:2px solid #5aa628;color:#fff;font-size:13px;line-height:20px}
.footer .contact{position:absolute;left:18px;top:18px}
.footer .credit{position:absolute;right:19px;top:18px;text-align:right}
.footer .credit b{font-weight:500}
.footer .credit u{font-weight:500}
</style>
</head>
<body>
<div class="stage">
  <div class="backdrop" role="img" aria-label="Sky and wheat field backdrop"></div>
  <div class="page">
    <header class="header">
      <div class="brand"><span class="brand-mark"></span><span class="brand-name">Downhorn</span></div>
      <div class="site-title">Pacific Downhorn Breeders Association</div>
    </header>

    <div class="hero" role="img" aria-label="Flock of sheep grazing in a green paddock">
      <div class="hero-arrow prev"><svg width="36" height="50" viewBox="0 0 36 50"><path d="M22 14 L13 25 L22 36" fill="none" stroke="#fff" stroke-width="2"/></svg></div>
      <div class="hero-arrow next"><svg width="36" height="50" viewBox="0 0 36 50"><path d="M14 14 L23 25 L14 36" fill="none" stroke="#fff" stroke-width="2"/></svg></div>
    </div>

    <nav class="nav">
      <a class="active" style="width:87px">Home</a>
      <a style="width:82px">About</a>
      <a class="active" style="width:83px">Search</a>
      <a style="width:153px">Member Services</a>
      <a style="width:111px">Stud Pages</a>
      <a style="width:77px">News</a>
      <a style="width:73px">Sales</a>
      <a style="width:73px">Links</a>
      <a style="width:99px;border-right:none">Contact</a>
    </nav>

    <div class="tiles">
      <div class="tile" style="left:18px"><div class="photo" role="img" aria-label="Helpline operator with headset" style="background:linear-gradient(135deg,#dfe8f0,#b9c9d6)"></div><div class="caption">Prime Lamb Helpline</div></div>
      <div class="tile" style="left:225px"><div class="photo" role="img" aria-label="Calendar page with a circled date" style="background:linear-gradient(135deg,#eef0f5,#c7ccd8)"></div><div class="caption">Our Events</div></div>
      <div class="tile" style="left:432px"><div class="photo" role="img" aria-label="Farmer in a hat standing with sheep" style="background:linear-gradient(135deg,#7a8a5a,#c8b8a0)"></div><div class="caption">Members Resources /<br>WebManager Login</div></div>
      <div class="tile" style="left:642px"><div class="photo" role="img" aria-label="News lettering beside a computer mouse" style="background:linear-gradient(135deg,#f4f4f4,#d0d0d0)"></div><div class="caption">Latest News</div></div>
    </div>

    <div class="dropdown">
      <a class="member">Member &nbsp;&gt;&gt;</a>
      <a class="stud">Stud &gt;&gt;</a>
    </div>

    <section class="content">
      <h2><b>Welcome</b> to our site</h2>
      <p class="intro">Lorem ipsum dolor sit amet, consectetur adipisicing elit, sed do eiusmod tempor incididunt<br>ut labore et dolore magna aliqua. Ut enim ad minim veniam, quis nostrud exercitation ullamco<br>laboris nisi ut aliquip ex ea commodo consequat. Lorem ipsum dolor sit amet, consectetur<br>adipisicing elit, sed do eiusmod tempor incididunt ut labore et dolore magna aliqua. Ut enim<br>ad minim veniam, quis nostrud exercitation ullamco laboris nisi ut aliquip ex ea commodo<br>consequat.</p>
      <p class="aims">The <span>Pacific Downhorn Breeders Association</span> aims to :</p>
      <ul class="aims-list">
        <li><svg width="11" height="10" viewBox="0 0 11 10"><path d="M1 5 L4 8 L10 1" fill="none" stroke="#4c9a14" stroke-width="2"/></svg>Lorem ipsum dolor sit amet, consectetur adipisicing elit, sed do eiusmod tempor<br>incididunt ut labore et dolore magna aliqua.</li>
        <li><svg width="11" height="10" viewBox="0 0 11 10"><path d="M1 5 L4 8 L10 1" fill="none" stroke="#4c9a14" stroke-width="2"/></svg>Lorem ipsum dolor sit amet, consectetur adipisicing elit, sed do eiusmod tempor<br>incididunt ut labore et dolore magna aliqua.</li>
      </ul>
    </section>

    <a class="btn">Know More
      <svg width="24" height="24" viewBox="0 0 24 24"><circle cx="12" cy="12" r="10.5" fill="none" stroke="#f6c27a" stroke-width="1.5"/><path d="M10 8 L14 12 L10 16" fill="none" stroke="#fff" stroke-width="1.5"/></svg>
    </a>

    <aside class="sidebar">
      <h2><b>Sponsors</b> we have</h2>
      <div class="sponsor-box">
        <div class="sponsor-bar top"><svg width="22" height="10" viewBox="0 0 22 10"><path d="M1 9 L11 1 L21 9" fill="none" stroke="#fff" stroke-width="1.5"/></svg></div>
        <div class="sponsor one"><span class="dot"></span>Fieldledger</div>
        <div class="sponsor two"><span class="dot"></span>Grainway Group</div>
        <div class="sponsor-bar bottom"><svg width="22" height="10" viewBox="0 0 22 10"><path d="M1 1 L11 9 L21 1" fill="none" stroke="#fff" stroke-width="1.5"/></svg></div>
      </div>
      <div class="social">
        <span class="sq"></span>
        <span class="divider"></span>
        <span class="count">31213 Followers</span>
        <span class="follow">Follow Us</span>
      </div>
    </aside>

    <footer class="footer">
      <div class="contact">
        PO Box 214, Harbourview, SA 5999<br>
        Phone : 08 5550 1234<br>
        Fax : 08 5550 1288<br>
        Email : info@downhornbreeders.org
      </div>
      <div class="credit">
        Copyright <b>Pacific Downhorn Breeders Association</b><br>
        Website design and development by <u>Webtide</u>
      </div>
    </footer>
  </div>
</div>
</body>
</html>
```